Coffee - Forum Design

Guarantee Payment:
I will start this project without guaranteeing payment. Until I receive 3 interested Freelancers emailing me "ready to start work", then I will guarantee payment.

About my website:
It will be a forum based website catering towards coffee and the like.

Requirements:
This will be a fun and simple design task. It requires the freelancer to take the dimensions of the following website:
https://brightlanehub.example/forums/
Please use the above website as your template.

And re-design it to suit my needs. Every single element in that the website above will be exactly the same. You can add personal touches to the design.

Theme:
Something fun and playful with a slight modern feel. Simple colours, nothing too crazy and bold. Preferably no dark colours.

Logo:
Is currently being finished off. Will be uploading in due course.

Thanks everyone and Good Luck,
Gord
PS. Send me a message if you have any queries.

NOTE: The PSD file must be CSS friendly while slicing the template.

Target Market(s)

Coffee & Cafe lovers of all types

Industry/Entity Type

Catering

Requirements
Must have
• Dimensions for each elements of the website can be seen in the following website, please use this as a guide:

```html
<!DOCTYPE html>
<html lang="en">
<head>
<meta charset="utf-8">
<title>Brew Nook – Forums</title>
<link rel="stylesheet" href="https://fonts.googleapis.com/css2?family=Yanone+Kaffeesatz:wght@400;500&family=Fauna+One&display=swap">
<style>
:root{
  --bar-brown:#5a3a14;
  --paper:#e9dcc3;
  --panel:#f9f7f2;
  --ink:#3b2a14;
  --ink-soft:#4a3a26;
  --line:#d9d4ca;
  --peach:#f8d196;
  --peach-text:#6b4518;
  --orange:#f39a1f;
  --footer-light:#f3d8a0;
  --footer-dark:#b97a2c;
  --field:#f4b04e;
}
*{box-sizing:border-box;margin:0;padding:0}
html,body{width:993px;height:1200px;overflow:hidden}
body{position:relative;background:linear-gradient(135deg,#eee2c9,var(--paper) 50%,#e2d1b0);font-family:"Fauna One",Georgia,serif;color:var(--ink)}
.abs{position:absolute}
.topbar{left:0;top:0;width:993px;height:29px;background:var(--bar-brown)}
.account-links{position:absolute;left:77px;top:9px;display:flex;gap:12px}
.account-links a{font:10px Arial,Helvetica,sans-serif;color:#fff;text-decoration:none;white-space:nowrap}
.field{position:absolute;top:3px;height:21px;background:var(--field);border:1px solid #c98a30;border-radius:3px;font:10px Arial,sans-serif;color:#4a2f0e;padding:4px 6px;white-space:nowrap}
.login-btn{position:absolute;left:844px;top:3px;width:42px;height:21px;background:linear-gradient(#6a6a6a,#3a3a3a);border-radius:3px;color:#fff;font:10px Arial,sans-serif;text-align:center;line-height:21px}
.side-art{background:radial-gradient(circle at 60% 40%,#9a6a3a,#c9a478 55%,rgba(233,220,195,0) 75%)}
.panel{left:65px;top:29px;width:840px;height:1155px;background:var(--panel)}
.header{left:65px;top:29px;width:840px;height:131px;box-shadow:0 3px 4px rgba(0,0,0,.08)}
.logo{left:80px;top:96px;font-family:"Fauna One",serif;font-size:32px;color:var(--ink);display:flex;align-items:center;gap:12px;white-space:nowrap}
.logo .dot{width:22px;height:22px;border-radius:50%;background:var(--ink)}
.nav-title{position:absolute;top:57px;transform:translateX(-50%);font:400 21px/22px "Yanone Kaffeesatz",sans-serif;color:var(--ink);letter-spacing:.4px;white-space:nowrap}
.nav-sub{position:absolute;top:79px;transform:translateX(-50%);font:9.5px/12px Arial,sans-serif;color:var(--ink-soft);white-space:nowrap}
.notice{left:84px;top:179px;width:803px;height:21px;background:var(--peach);border-radius:2px;font-size:11px;color:var(--ink);padding:4px 9px;display:flex;justify-content:space-between;white-space:nowrap}
.topics{left:84px;top:215px;width:561px;list-style:none;border-top:1px solid var(--line)}
.topic{position:relative;border-bottom:1px solid var(--line);padding-left:5px;white-space:nowrap}
.topic h3{font-weight:400;font-size:13px;color:var(--ink);padding-top:6px}
.topic .product{font-size:9.5px;margin-top:12px}
.topic .meta{font-size:9.5px;margin-top:8px}
.avatar{position:absolute;right:4px;top:10px;width:38px;height:38px;background:linear-gradient(#d6d6d6,#bcbcbc)}
.load-more{left:86px;top:882px;width:569px;height:32px;border:1px solid #a56a22;border-radius:4px;background:linear-gradient(#fbdba8,#e9a94e);font:14px Arial,sans-serif;color:#1d1306;text-align:center;line-height:30px}
.search{left:666px;top:214px;width:162px;height:20px;border:1px solid #ccc;background:#fff;font-size:9.5px;color:#777;padding:3px 5px}
.side-h{position:absolute;left:671px;font-size:12.5px;color:var(--ink)}
.check{position:absolute;left:675px;font-size:9.5px;display:flex;align-items:center;gap:6px;white-space:nowrap}
.check i{width:9px;height:9px;border:1px solid #999;background:#fff;display:block}
.rule{position:absolute;left:664px;width:223px;height:1px;background:var(--line)}
.slider-track{left:676px;top:469px;width:197px;height:8px;border-radius:4px;background:linear-gradient(#ffb347,var(--orange) 50%,#e07c0a)}
.slider-knob{position:absolute;top:462px;width:24px;height:24px;border-radius:3px;background:linear-gradient(#e6cfa6,#b89464);border:1px solid #9c7a4c}
.info{left:672px;top:527px;width:205px;height:229px;background:var(--peach);border-radius:4px;padding:16px 12px;font-size:11.5px;line-height:17.8px;color:var(--peach-text)}
.footer{left:70px;top:958px;width:830px;height:221px;background:radial-gradient(ellipse at 50% 60%,var(--footer-light),#e8b767 55%,var(--footer-dark));box-shadow:inset 0 0 14px rgba(90,50,10,.5)}
.f-col{position:absolute;top:1010px}
.f-col h4{font:400 19px "Yanone Kaffeesatz",sans-serif;color:#2a1a08;margin-bottom:6px}
.f-col a{display:block;font:9.5px/13.5px Arial,sans-serif;color:#1e1306;text-decoration:none;white-space:nowrap}
.copyright{left:70px;width:830px;top:1137px;text-align:center;font:9px Arial,sans-serif;color:#1e1306}
</style>
</head>
<body>
<div class="abs side-art" role="img" aria-label="Coffee cups and beans illustration" style="left:905px;top:30px;width:88px;height:350px"></div>
<div class="abs side-art" role="img" aria-label="Coffee cup illustration" style="left:0;top:250px;width:65px;height:170px"></div>

<header>
  <div class="abs topbar">
    <div class="account-links"><a>Setup My Account</a><a>Forgot Password?</a></div>
    <div class="field" style="left:565px;width:168px">Email or phone no</div>
    <div class="field" style="left:739px;width:100px">Password</div>
    <div class="login-btn">Login</div>
  </div>
</header>

<div class="abs panel"></div>
<div class="abs header"></div>
<div class="abs logo"><span class="dot"></span>Brew Nook</div>
<nav>
  <div class="nav-title" style="left:373px">PRODUCTS</div><div class="nav-sub" style="left:369px">plugin &amp; themes</div>
  <div class="nav-title" style="left:493px">SERVICES</div><div class="nav-sub" style="left:471px">what we can do for you</div>
  <div class="nav-title" style="left:600px">FORUMS</div><div class="nav-sub" style="left:579px">community &amp; support</div>
  <div class="nav-title" style="left:719px">HELP</div><div class="nav-sub" style="left:688px">community &amp; support</div>
  <div class="nav-title" style="left:798px">BLOG</div><div class="nav-sub" style="left:781px">news &amp; articles</div>
  <div class="nav-title" style="left:860px">CONTACT</div><div class="nav-sub" style="left:859px">drop us a line</div>
</nav>

<main>
  <div class="abs notice"><span>There are 3188 total results, with 50 results per page.</span><span>x</span></div>
  <ul class="abs topics">
    <li class="topic" style="height:71px"><h3>Lorem ipsum dolor sit amet</h3><p class="product">BillPress</p><p class="meta">Freshness 31 minutes ago, Posts: 2</p><div class="avatar" role="img" aria-label="Member avatar"></div></li>
    <li class="topic" style="height:76px"><h3>Lorem ipsum dolor sit amet</h3><p class="product">BillPress</p><p class="meta">Freshness 31 minutes ago, Posts: 2</p><div class="avatar" role="img" aria-label="Member avatar"></div></li>
    <li class="topic" style="height:80px"><h3 style="padding-top:13px">Lorem ipsum dolor sit amet</h3><p class="product">BillPress</p><p class="meta">Freshness 31 minutes ago, Posts: 2</p><div class="avatar" style="top:16px" role="img" aria-label="Member avatar"></div></li>
    <li class="topic" style="height:81px"><h3 style="padding-top:13px">Lorem ipsum dolor sit amet</h3><p class="product">BillPress</p><p class="meta">Freshness 31 minutes ago, Posts: 2</p><div class="avatar" style="top:18px" role="img" aria-label="Member avatar"></div></li>
    <li class="topic" style="height:80px"><h3 style="padding-top:13px">Lorem ipsum dolor sit amet</h3><p class="product">BillPress</p><p class="meta">Freshness 31 minutes ago, Posts: 2</p><div class="avatar" style="top:18px" role="img" aria-label="Member avatar"></div></li>
    <li class="topic" style="height:80px"><h3 style="padding-top:13px">Lorem ipsum dolor sit amet</h3><p class="product">BillPress</p><p class="meta">Freshness 31 minutes ago, Posts: 2</p><div class="avatar" style="top:18px" role="img" aria-label="Member avatar"></div></li>
    <li class="topic" style="height:81px"><h3 style="padding-top:13px">Lorem ipsum dolor sit amet</h3><p class="product">BillPress</p><p class="meta">Freshness 31 minutes ago, Posts: 2</p><div class="avatar" style="top:18px" role="img" aria-label="Member avatar"></div></li>
    <li class="topic" style="height:80px"><h3 style="padding-top:13px">Lorem ipsum dolor sit amet</h3><p class="product">BillPress</p><p class="meta">Freshness 31 minutes ago, Posts: 2</p><div class="avatar" style="top:18px" role="img" aria-label="Member avatar"></div></li>
  </ul>
  <div class="abs load-more">Load 50 More</div>
</main>

<aside>
  <div class="abs search">SearchTopics...</div>
  <div class="side-h" style="top:246px">Products</div>
  <div class="check" style="top:269px"><i></i>SitePlot2307</div>
  <div class="check" style="top:287px"><i></i>BillPress425</div>
  <div class="check" style="top:305px"><i></i>The Summit Premium Theme270</div>
  <div class="check" style="top:322px"><i></i>ClientDesk186</div>
  <div class="rule" style="top:347px"></div>
  <div class="side-h" style="top:357px">Topic Types</div>
  <div class="check" style="top:380px"><i></i>Regular2794</div>
  <div class="check" style="top:398px"><i></i>Premium394</div>
  <div class="rule" style="top:426px"></div>
  <div class="side-h" style="top:436px">Topic Post</div>
  <div class="abs slider-track"></div>
  <div class="slider-knob" style="left:673px"></div>
  <div class="slider-knob" style="left:853px"></div>
  <div class="rule" style="top:514px"></div>
  <div class="abs info">This is a community forum for discussion of SitePlot, BillPress, ClientDesk, as well as general SiteCraft and web-related issues. If you are seeking support, you may ask questions directly to our staff by utilizing the Premium Question feature, or you can read more about our support policy.</div>
</aside>

<footer>
  <div class="abs footer"></div>
  <div class="f-col" style="left:164px"><h4>Home</h4></div>
  <div class="f-col" style="left:307px"><h4>Service</h4><a>Theme and Plugin EULA</a><a>Web Hosting AUP</a></div>
  <div class="f-col" style="left:461px"><h4>Products</h4><a>ClientDesk</a><a>SitePlot</a><a>BillPress</a></div>
  <div class="f-col" style="left:621px"><h4>Forums</h4><a>Forum and support policy</a></div>
  <div class="f-col" style="left:775px"><h4>Help</h4><a>ClientDesk</a><a>SitePlot</a><a>BillPress</a></div>
  <div class="abs copyright">©2012, All Rights Reserved, Brew Nook</div>
</footer>
</body>
</html>
```